Business card for Tolvery Anesthesia LLC

This is for a business care for Tolvery Anesthesia LLC. Dr. Lisbeth Tolvery, CRNA, DNAP is the sole provider in the LLC. Business address is 4718 N Brackley Street,
Oakhaven, PA 17342
CRNA stands for certified registered nurse anesthetist
"Keeping you safe and comfortable"
I plan to give this business card to the patients that I provide anesthesia to.
Creative design that ties into Anesthesia. Calm soothing colors.

Target Market(s)

Business card for my patients.

Industry/Entity Type

Medicine

Contact Information for Business Card

Creative, professional, eye catching

Logo Text

Tolvery Anesthesia

Font styles to use
Serif
Script

Colors

Designer to choose colors to be used in the design.

Requirements
Must have
• Tolvery Anesthesia
• Dr. Lisbeth Tolvery, CRNA, DNAP
• tolvery.anesthesia@ quillmail.net
Nice to have
• "Keeping you safe and comfortable"
Should not have
• phone number

```html
<!DOCTYPE html>
<html lang="en">
<head>
<meta charset="utf-8">
<title>Tolvery Anesthesia LLC – Business Card</title>
<link rel="stylesheet" href="https://fonts.googleapis.com/css2?family=Cinzel:wght@400;600&family=Lato:wght@400;700&display=swap">
<style>
  :root {
    --backdrop: #1c1c1e;
    --navy: #27528a;
    --green: #5e9e2b;
    --paper: #f5f5f5;
    --rule: #dcdcdc;
    --ink: #3a3a3a;
    --white: #ffffff;
  }
  * { box-sizing: border-box; margin: 0; padding: 0; }
  html, body {
    width: 1200px; height: 900px; overflow: hidden;
    background: var(--backdrop);
  }
  .stage {
    width: 1200px; height: 900px;
    display: flex; flex-direction: column; align-items: center; justify-content: center;
    gap: 44px;
  }
  .card {
    position: relative;
    width: 560px; height: 320px;
    border-radius: 22px;
    overflow: hidden;
    box-shadow: 0 10px 28px rgba(0,0,0,.5);
  }

  /* Front */
  .card--front {
    background: var(--navy);
    display: flex; align-items: center; justify-content: center;
  }
  .brand { display: flex; align-items: center; gap: 16px; }
  .brand__dot {
    width: 86px; height: 86px; border-radius: 50%;
    background: var(--white); flex: none;
  }
  .brand__name {
    font-family: "Cinzel", serif; font-weight: 400;
    font-size: 30px; line-height: 1.05; letter-spacing: 1px;
    color: var(--white);
  }

  /* Back */
  .card--back { background: var(--paper); }
  .card--back .brand { position: absolute; left: 188px; top: 40px; gap: 12px; }
  .card--back .brand__dot { width: 62px; height: 62px; background: var(--navy); }
  .card--back .brand__name { font-size: 24px; color: var(--navy); }

  .rule {
    position: absolute; left: 40px; right: 40px; height: 1px; background: var(--rule);
  }
  .rule--top { top: 126px; }
  .rule--mid { top: 180px; }

  .person {
    position: absolute; left: 40px; top: 142px;
    font-family: "Cinzel", serif; font-weight: 600;
    color: var(--navy); line-height: 26px;
  }
  .person__name { font-size: 22px; letter-spacing: 1px; }
  .person__creds { font-size: 13px; font-weight: 400; letter-spacing: 1px; }

  .contact {
    position: absolute; left: 40px; top: 188px;
    list-style: none;
    font-family: "Lato", sans-serif; font-size: 15px; color: var(--ink);
  }
  .contact__item { display: flex; align-items: center; gap: 9px; height: 26px; }
  .contact__icon { width: 15px; height: 15px; flex: none; }

  .tagline-band {
    position: absolute; left: 0; right: 0; bottom: 0; height: 92px;
    background: var(--green);
    clip-path: polygon(0 42%, 100% 0, 100% 100%, 0 100%);
    display: flex; align-items: flex-end;
    padding: 0 0 16px 40px;
  }
  .tagline {
    font-family: "Lato", sans-serif; font-size: 15px; letter-spacing: .6px;
    text-transform: uppercase; color: var(--white);
  }
</style>
</head>
<body>
<main class="stage">

  <section class="card card--front" aria-label="Card front">
    <div class="brand">
      <span class="brand__dot"></span>
      <span class="brand__name">Tolvery<br>Anesthesia LLC</span>
    </div>
  </section>

  <section class="card card--back" aria-label="Card back">
    <div class="brand">
      <span class="brand__dot"></span>
      <span class="brand__name">Tolvery<br>Anesthesia LLC</span>
    </div>

    <div class="rule rule--top"></div>

    <p class="person">
      <span class="person__name">Dr. Lisbeth Tolvery</span><span class="person__creds">, CRNA, DNAP</span>
    </p>

    <div class="rule rule--mid"></div>

    <ul class="contact">
      <li class="contact__item">
        <svg class="contact__icon" viewBox="0 0 16 16" aria-hidden="true">
          <rect x="1" y="3" width="14" height="10" rx="1" fill="#5e9e2b"/>
          <path d="M1.5 3.8 8 9l6.5-5.2" fill="none" stroke="#fff" stroke-width="1.3"/>
        </svg>
        tolvery.anesthesia@ quillmail.net
      </li>
      <li class="contact__item">
        <svg class="contact__icon" viewBox="0 0 16 16" aria-hidden="true">
          <path d="M8 1a5 5 0 0 0-5 5c0 3.6 5 9 5 9s5-5.4 5-9a5 5 0 0 0-5-5z" fill="#5e9e2b"/>
          <circle cx="8" cy="6" r="2" fill="#fff"/>
        </svg>
        4718 N Brackley Street Oakhaven, PA 17342
      </li>
    </ul>

    <div class="tagline-band">
      <p class="tagline">Keeping you safe and comfortable</p>
    </div>
  </section>

</main>
</body>
</html>
```